依頼詳細
〇イメージは可愛い系ではなくカッコいい系でお願いします。

〇サイズは5号~17号、ツイードスーツ2点セットからパンツスーツ、ワンピーススーツ等の3点セットまで豊富なバリエーションをお得な価格で提供している事をアピールしたい。

〇自宅で試着して気に入った方を購入できる試着券を用意

〇必要ならモデル写真(添付以外の)を提供します。

〇上記要素は可能な限り入れて欲しいですが、盛りだくさんになるようなら全ての要素は必須ではありません。
記載項目
サイト名:クロシェ・ガーデン
ロゴを使用してください。
サイズ
• 横2000x縦1200、横750x縦300、
希望イメージ
シンプル 複雑
単色 カラフル
暗い 明るい
日常 高級
遊び心 厳粛
未来的 伝統的
女性的 男性的
希望する色
赤系、青系、無彩色系
納品ファイル
• フォトショップ形式 (.psd)
補足説明
スマホページにも掲載予定のため、スマホで読めるフォントの大きさへの対応をお願いします。
■ 選んだ理由

弊社の製品イメージを良くとらえていただいていると感じられるご提案を選びました。
ご提案の中には秀逸なコピーのご提案もあり悩みましたが総合点での判定とさせていただきました。

■ 提案者全員のお礼・コメント

色んな観点からバラエティー豊かなご提案をいただき感謝しております。
発注者としましては、あまり細かい要求は皆様のデザイン性を縛ってしまう恐れありと思い
大まかなイメージでお伝えしておりましたが、それでよかったのかと反省しております。

また、機会がありましたらご応募頂けますようお願い申し上げます。

```html
<!DOCTYPE html>
<html lang="ja">
<head>
<meta charset="utf-8">
<title>クロシェ・ガーデン バナー</title>
<link rel="stylesheet" href="https://fonts.googleapis.com/css2?family=Shippori+Mincho+B1:wght@700;800&family=Noto+Sans+JP:wght@500;700;900&display=swap">
<style>
  :root {
    --wine: #8a0c1f;
    --wine-deep: #6f0716;
    --blush: #f1d6db;
    --rose: #d89aa5;
    --white: #ffffff;
    --ink: #2a2a2a;
  }
  * { box-sizing: border-box; margin: 0; padding: 0; }
  html, body { width: 1200px; height: 480px; overflow: hidden; background: var(--wine); }
  .banner { position: relative; width: 1200px; height: 480px; background: var(--wine); font-family: "Shippori Mincho B1", serif; }

  .offer { position: absolute; left: 34px; top: 22px; width: 674px; height: 434px; background: var(--blush); }
  .offer-lines { position: absolute; left: 0; top: 12px; width: 100%; text-align: center; color: var(--wine-deep); font-weight: 800; font-size: 35px; line-height: 44px; letter-spacing: 1px; }
  .offer-headline { position: absolute; left: 24px; top: 150px; width: 608px; height: 138px; background: var(--wine); color: var(--white); text-align: center; font-weight: 800; font-size: 47px; line-height: 58px; padding-top: 10px; letter-spacing: 1px; box-shadow: 6px 6px 0 rgba(0,0,0,.18); }

  .trial { position: absolute; left: 24px; top: 318px; width: 596px; height: 92px; background: var(--white); border: 3px solid var(--wine); font-family: "Noto Sans JP", sans-serif; }
  .trial-home { position: absolute; left: 8px; top: 8px; width: 28px; color: var(--wine); font-weight: 900; font-size: 24px; line-height: 28px; text-align: center; }
  .trial-big { position: absolute; left: 40px; top: -6px; color: var(--wine); font-weight: 900; font-size: 80px; line-height: 96px; letter-spacing: 2px; }
  .trial-note { position: absolute; left: 232px; top: 4px; color: var(--wine); font-weight: 700; font-size: 25px; line-height: 32px; }
  .trial-ticket { position: absolute; left: 232px; top: 40px; width: 300px; height: 42px; background: var(--wine); color: var(--white); font-weight: 700; font-size: 30px; line-height: 42px; text-align: center; }
  .trial-cursor { position: absolute; left: 510px; top: 40px; width: 76px; height: 56px; }

  .gallery-photo { position: absolute; left: 746px; top: 22px; width: 436px; height: 434px;
    background: linear-gradient(90deg, #f4f1ee 0%, #e9e6e3 30%, #c9cbd0 45%, #2b2a2c 55%, #d0d2d6 68%, #f2efec 85%, #f7f5f2 100%); }
  .gallery-gap { position: absolute; background: var(--wine); }
  .tile { position: absolute; }
  .tile-plain { left: 746px; top: 22px; width: 142px; height: 140px; background: var(--rose); }
  .tile-brand { left: 746px; top: 319px; width: 142px; height: 137px; background: var(--wine); border: 2px solid var(--rose); display: flex; align-items: center; justify-content: center; text-align: center; color: var(--white); font-weight: 700; font-size: 19px; line-height: 26px; }
  .tile-name { left: 1050px; top: 319px; width: 132px; height: 137px; background: var(--rose); color: var(--wine-deep); font-family: "Noto Sans JP", sans-serif; font-weight: 500; font-size: 18px; line-height: 26px; padding: 40px 0 0 16px; }
</style>
</head>
<body>
<div class="banner">
  <section class="offer">
    <p class="offer-lines">ツイードスーツ 2点セット<br>パンツスーツ<br>ワンピーススーツ等の3点セット</p>
    <h1 class="offer-headline">豊富なバリエーションを<br>お得な価格で</h1>
    <div class="trial">
      <span class="trial-home">自宅で</span>
      <span class="trial-big">試着</span>
      <span class="trial-note">気に入った方を購入できる</span>
      <span class="trial-ticket">試着ticket</span>
      <svg class="trial-cursor" viewBox="0 0 76 56" aria-hidden="true">
        <path d="M6 22 L46 8 L40 18 L72 34 L64 46 L32 30 L26 40 Z" fill="#ffffff" stroke="#555" stroke-width="2.5" stroke-linejoin="round"/>
      </svg>
    </div>
  </section>

  <div class="gallery-photo" role="img" aria-label="黒い帽子をかぶり、ツイードジャケットを着た女性モデルの写真"></div>
  <div class="gallery-gap" style="left:888px;top:22px;width:12px;height:434px"></div>
  <div class="gallery-gap" style="left:1038px;top:22px;width:12px;height:434px"></div>
  <div class="gallery-gap" style="left:746px;top:162px;width:436px;height:10px"></div>
  <div class="gallery-gap" style="left:746px;top:310px;width:436px;height:9px"></div>

  <div class="tile tile-plain"></div>
  <div class="tile tile-brand">クロシェ・<br>ガーデン</div>
  <div class="tile tile-name">クロシェ・<br>ガーデン</div>
</div>
</body>
</html>
```